Delmer's Pressure Washing Services

Starting a pressure washing business on my own in Central Valley California, not too much experience so affordable, I do houses, fences, driveways, cars, trailers, RVs. Planning to make this full-time hoping clientele picks up after having a nice business card. Design doesn't have to be flashy, more to the point, I like simplistic/personable. I do not want something exhausting to look at or with too much going on.

Target Market(s)

Residential, Commercial

Industry/Entity Type

Pressure Washing

Contact Information for Business Card

avalible Services

Font styles to use
Sans Serif

Colors
0054AA
0677BA
7BADD7
CADEEF
E8F1F8
0094D4
00A9DD
6FCCEA
C7EBF8
E9F6FB
00AB8E
00BBA5
67D7C9
C6EFE9
E9F9F6

```html
<!DOCTYPE html>
<html lang="en">
<head>
<meta charset="utf-8">
<title>Delmer's Pressure Washing Services – Business Card</title>
<link href="https://fonts.googleapis.com/css2?family=Poppins:wght@400;500;600&display=swap" rel="stylesheet">
<style>
  :root {
    --page: #e6e6e6;
    --navy: #0f2430;
    --navy-back: #1c3947;
    --blue-deep: #0677ba;
    --blue: #0094d4;
    --blue-bright: #00a9dd;
    --blue-soft: #6fccea;
    --blue-pale: #7badd7;
    --text-light: #8fd3ee;
  }
  html, body {
    margin: 0;
    padding: 0;
    width: 1200px;
    height: 2562px;
    overflow: hidden;
    background: var(--page);
    font-family: "Poppins", sans-serif;
  }
  .sheet {
    position: relative;
    width: 1200px;
    height: 2562px;
  }
  .card {
    position: absolute;
    left: 150px;
    width: 900px;
    height: 514px;
    border-radius: 28px;
    overflow: hidden;
    box-shadow: 0 18px 40px rgba(0, 0, 0, 0.18);
  }
  .card--front { top: 700px; background: var(--navy); }
  .card--back  { top: 1348px; background: var(--navy-back); }

  .card__art {
    position: absolute;
    inset: 0;
    width: 100%;
    height: 100%;
  }

  .brand {
    position: absolute;
    text-align: center;
    color: var(--blue-bright);
    font-weight: 600;
    line-height: 1;
  }
  .brand__name {
    display: block;
    font-size: 92px;
    letter-spacing: 1px;
  }
  .brand__tagline {
    display: block;
    margin-top: 10px;
    font-size: 17px;
    letter-spacing: 5px;
    text-transform: uppercase;
  }
  .brand__dot {
    display: inline-block;
    width: 22px;
    height: 22px;
    border-radius: 50%;
    background: var(--blue-bright);
    margin-right: 14px;
    vertical-align: 18px;
  }
  .card--front .brand { left: 360px; top: 190px; width: 460px; }
  .card--front .brand__name { font-size: 78px; }
  .card--front .brand__tagline { font-size: 14px; letter-spacing: 4px; }
  .card--back .brand { left: 0; right: 0; top: 190px; }

  .contact {
    position: absolute;
    left: 56px;
    top: 282px;
    color: var(--text-light);
  }
  .contact__name {
    margin: 0 0 12px;
    font-size: 26px;
    font-weight: 600;
    letter-spacing: 0.5px;
  }
  .contact__line {
    display: flex;
    align-items: center;
    gap: 10px;
    margin: 0 0 4px;
    font-size: 19px;
    font-weight: 400;
  }
  .contact__line svg { width: 16px; height: 16px; flex: none; }
  .services {
    position: absolute;
    left: 56px;
    top: 430px;
    margin: 0;
    color: var(--text-light);
    font-size: 19px;
  }
</style>
</head>
<body>
<main class="sheet">

  <section class="card card--front" aria-label="Business card front">
    <svg class="card__art" viewBox="0 0 900 514" aria-hidden="true">
      <defs>
        <linearGradient id="wave-top" x1="0" y1="0" x2="1" y2="1">
          <stop offset="0" stop-color="#6fccea"/>
          <stop offset="1" stop-color="#0677ba"/>
        </linearGradient>
      </defs>
      <!-- top wave band -->
      <path d="M310 0 H900 V150 C860 110 800 90 740 110 C690 125 650 90 600 80 C540 68 520 110 460 100 C400 90 370 50 310 0 Z" fill="url(#wave-top)"/>
      <path d="M400 0 H900 V70 C850 60 800 70 760 60 C720 50 700 20 650 25 C600 30 560 45 520 35 C470 22 440 10 400 0 Z" fill="#7badd7" opacity="0.75"/>
      <!-- bottom right sweep -->
      <path d="M900 230 C880 360 800 460 660 514 H900 Z" fill="#6fccea"/>
      <path d="M900 260 C885 370 820 455 700 514 H680 C810 455 880 360 900 230 Z" fill="#7badd7"/>
      <!-- circles -->
      <circle cx="10" cy="60" r="58" fill="#0094d4"/>
      <circle cx="130" cy="28" r="52" fill="#7badd7"/>
      <circle cx="115" cy="120" r="26" fill="#0094d4"/>
      <circle cx="22" cy="230" r="14" fill="#0094d4"/>
    </svg>

    <div class="brand">
      <span class="brand__name">Delmer's</span>
      <span class="brand__tagline">Pressure Washing Services</span>
    </div>

    <div class="contact">
      <p class="contact__name">DELMER RUIZ</p>
      <p class="contact__line">
        <svg viewBox="0 0 16 16"><path d="M4 1 L6.5 1 L7.5 5 L5.5 6.5 C6.5 8.5 7.5 9.5 9.5 10.5 L11 8.5 L15 9.5 V12 C15 13.5 13.5 15 12 15 C6 15 1 10 1 4 C1 2.5 2.5 1 4 1 Z" fill="#0094d4"/></svg>
        2095550148
      </p>
      <p class="contact__line">
        <svg viewBox="0 0 16 16"><rect x="1" y="3" width="14" height="10" rx="1.5" fill="#0094d4"/><path d="M1.5 4 L8 9 L14.5 4" stroke="#0f2430" stroke-width="1.4" fill="none"/></svg>
        hello@delmerwash.com
      </p>
    </div>
    <p class="services">Houses | Fences | Driveways | Cars | Trailers | RVs clening</p>
  </section>

  <section class="card card--back" aria-label="Business card back">
    <svg class="card__art" viewBox="0 0 900 514" role="img" aria-label="Faint scattered bubble pattern across the dark background">
      <defs>
        <radialGradient id="back-glow" cx="0.6" cy="0.55" r="0.7">
          <stop offset="0" stop-color="#24485a"/>
          <stop offset="1" stop-color="#1a3643"/>
        </radialGradient>
      </defs>
      <rect width="900" height="514" fill="url(#back-glow)"/>
    </svg>
    <div class="brand">
      <span class="brand__name"><span class="brand__dot"></span>Delmer's</span>
      <span class="brand__tagline">Pressure Washing Services</span>
    </div>
  </section>

</main>
</body>
</html>
```